International Legal Service Company needs Letterhead Design

Put my new Logo into Letterhead Design, using updated telephone number, e-mail address and website. Current letterhead and updated information which i want you to include my new letterhead attached herewith. Of course, my new Logo attached herein. Also, you can use slogan "Total Legal Outsourcing Solutions For Multinational Businesses"

It Company

```html
<!DOCTYPE html>
<html lang="en">
<head>
<meta charset="utf-8">
<title>Meridian Counsel Partners Inc — Letterhead</title>
<link rel="stylesheet" href="https://fonts.googleapis.com/css2?family=Roboto:wght@500&family=Roboto+Condensed:wght@400&family=Tinos:wght@400;700&display=swap">
<style>
  :root {
    --paper: #ffffff;
    --brand-blue: #1f4f8f;
    --contact-blue: #2a4f86;
    --body-text: #555555;
    --heading-text: #333333;
    --faint-mark: #efefef;
    --signature-tone: #e9e9e9;
  }
  * { margin: 0; padding: 0; box-sizing: border-box; }
  html, body { width: 942px; height: 1200px; overflow: hidden; background: var(--paper); }
  .letterhead { position: relative; width: 942px; height: 1200px; background: var(--paper); overflow: hidden; }

  .brand { position: absolute; left: 74px; top: 44px; display: flex; align-items: center; gap: 14px; }
  .brand-dot { width: 104px; height: 104px; border-radius: 50%; background: var(--brand-blue); }
  .brand-name { font-family: "Roboto", Arial, sans-serif; font-weight: 500; font-size: 32px; line-height: 36px; color: var(--brand-blue); }

  .contact { position: absolute; right: 79px; top: 54px; text-align: right; font-family: "Roboto Condensed", Arial, sans-serif; font-size: 12.5px; line-height: 13.6px; letter-spacing: 0.6px; color: var(--contact-blue); list-style: none; }

  .meta { position: absolute; left: 127px; top: 200px; font-family: "Tinos", "Times New Roman", serif; font-size: 12.5px; color: var(--heading-text); }
  .meta p { line-height: 24px; }
  .meta strong { font-weight: 700; }

  .letter-body { position: absolute; left: 127px; top: 272px; width: 736px; font-family: "Tinos", "Times New Roman", serif; font-size: 11.6px; color: var(--body-text); }
  .salutation { line-height: 24px; margin-bottom: 0; }
  .letter-body .paragraph { line-height: 25px; text-align: justify; margin-bottom: 24px; }

  .sign-off { position: absolute; left: 127px; top: 876px; font-family: "Tinos", "Times New Roman", serif; font-size: 11.6px; color: var(--heading-text); line-height: 16px; }

  .signature { position: absolute; left: 122px; top: 960px; width: 260px; height: 120px; background: var(--signature-tone); border-radius: 4px; }

  .faint-mark { position: absolute; left: 686px; top: 896px; width: 250px; height: 250px; border-radius: 50%; background: var(--faint-mark); }
</style>
</head>
<body>
<main class="letterhead">
  <header>
    <div class="brand">
      <span class="brand-dot"></span>
      <div class="brand-name">Meridian Counsel<br>Partners Inc</div>
    </div>
    <ul class="contact">
      <li>418 Harbor Crest Avenue</li>
      <li>Suite 210</li>
      <li>Fairview, OR 97024</li>
      <li>555-204-7713</li>
      <li>555-318-6640</li>
      <li>office@meridiancounsel.example</li>
      <li>meridiancounsel.example.com</li>
    </ul>
  </header>

  <section class="meta">
    <p><strong>Data :</strong> Mon , 25 / 3 / 2013</p>
    <p><strong>Recipient :</strong> Mr. Alan Reed Whitmore</p>
  </section>

  <article class="letter-body">
    <p class="salutation">Dear Mr. Alan Reed</p>
    <p class="paragraph">LoTrem ipsum dolor sit amet, consectetur adipiscing elit. Praesent vulputate, neque ac accumsan suscipit, justo turpis volutpat nisl, tempus fermentum eros tortor et elit. Vivamus porttitor faucibus gravida. Quisque pharetra gravida luctus. Donec eget turpis libero. Ut ac dolor urna, quis tempor nunc. Donec vitae mauris purus, euismod eleifend nulla. Lorem ipsum dolor sit amet, consectetur adipiscing elit. Donec ut purus tellus. Aenean quis dignissim lacus. Vestibulum suscipit vehicula cursus. Suspendisse potenti. Ut in sem nisi. Sed et massa leo.</p>
    <p class="paragraph">Fusce varius libero vel risus condimentum suscipit. Nullam tristique ultrices massa a volutpat. Donec sed dictum metus. Curabitur fringilla nibh eu ligula pharetra a interdum quam aliquam. Maecenas aliquam elit eu orci rutrum molestie. Proin nisl justo, varius a volutpat nec, ultricies sed sem. Nam sit amet imperdiet sem. Phasellus vitae mauris odio. Etiam in purus dui. Etiam ultricies, ante vel iaculis sodales, arcu leo adipiscing leo, sit amet mollis dui nisi non quam.</p>
    <p class="paragraph">Suspendisse sagittis laoreet dolor, vitae rhoncus arcu volutpat quis. Vestibulum at placerat dolor. Vivamus eu lacus ut enim molestie consectetur. Quisque ac lorem vel orci sagittis sollicitudin. Nunc ut quam sem, quis volutpat libero. Cum sociis natoque penatibus et magnis dis parturient montes, nascetur ridiculus mus. Vestibulum ante ipsum primis in faucibus orci luctus et ultrices posuere cubilia Curae; Donec tempor velit in velit feugiat sit amet vulputate nisl posuere..</p>
  </article>

  <footer class="sign-off">
    <p>DANIEL MARSH</p>
    <p>General director</p>
  </footer>

  <div class="signature" role="img" aria-label="Handwritten signature of the general director"></div>
  <div class="faint-mark" aria-hidden="true"></div>
</main>
</body>
</html>
```